New Business Card Design Project

I would like to purchase a customized version of a design you have previously submitted - https://www.plorvexa.com/design/7314826<br/><br/>I would like to incorporate the attached Images for my fitness company "TrelmoKor Athletics". My initial services is personal training and athletic performance. I would like a card that has one a shiny black side with the silver logo and the side with a white background utilizing the gold logo. On the white side, put "Sports Performance and Functional Strength Training" under the logo.
Industry/Entity Type
Fitness
Contact Information for Business Card
Quillan Morrow
Owner and Trainer
555.271.9384
quillan.morrow@trelmokorathletics.com
Look and feel
Each slider illustrates characteristics of the customer's brand and the style your logo design should communicate.

```html
<!DOCTYPE html>
<html lang="en">
<head>
<meta charset="utf-8">
<title>TrelmoKor Athletics – Business Card</title>
<link rel="stylesheet" href="https://fonts.googleapis.com/css2?family=Montserrat:wght@400;500;600&display=swap">
<style>
  :root {
    --page-bg: #e9e7e3;
    --card-black: #1f1f1f;
    --card-black-deep: #121212;
    --card-white: #ffffff;
    --silver: #d9d9d9;
    --gold: #8a6b32;
    --gold-light: #b69658;
    --ink: #1c1c1c;
    --rule: #8c8c8c;
  }
  * { margin: 0; padding: 0; box-sizing: border-box; }
  html, body {
    width: 1200px; height: 1021px; overflow: hidden;
    background: var(--page-bg);
    font-family: "Montserrat", Arial, sans-serif;
  }
  .sheet {
    width: 1200px; height: 1021px;
    display: flex; flex-direction: column; align-items: center; justify-content: center;
    gap: 40px;
  }
  .card {
    width: 800px; height: 457px; position: relative; overflow: hidden;
    box-shadow: 0 6px 18px rgba(0,0,0,.18);
  }
  /* Front: shiny black */
  .card-front {
    background: linear-gradient(160deg, #2c2c2c 0%, var(--card-black) 45%, var(--card-black-deep) 100%);
    color: var(--silver);
    display: flex; flex-direction: column; align-items: center; justify-content: center;
  }
  .card-front .sheen {
    position: absolute; inset: 0;
    background: radial-gradient(ellipse at 85% 60%, rgba(255,255,255,.06), transparent 60%);
  }
  .front-mark {
    width: 150px; height: 150px; border-radius: 50%;
    background: radial-gradient(circle at 40% 35%, #f2f2f2, #9d9d9d 70%, #6e6e6e);
    border: 4px solid #e6e6e6;
    margin-bottom: 26px; position: relative;
  }
  .front-name {
    font-weight: 600; font-size: 38px; letter-spacing: 4px; color: #f0f0f0; position: relative;
  }
  .front-tagline {
    font-size: 19px; margin-top: 8px; color: var(--silver); position: relative; letter-spacing: .3px;
  }
  /* Back: white */
  .card-back { background: var(--card-white); color: var(--ink); }
  .brand-block {
    position: absolute; left: 45px; top: 60px; width: 230px;
    display: flex; flex-direction: column; align-items: center;
  }
  .back-mark {
    width: 190px; height: 190px; border-radius: 50%;
    background: radial-gradient(circle at 40% 35%, #d9c08d, var(--gold-light) 45%, var(--gold) 80%);
    border: 6px solid #3a3a3a;
  }
  .back-name {
    margin-top: 14px; font-weight: 600; font-size: 18px; color: var(--ink); letter-spacing: .5px;
    white-space: nowrap;
  }
  .divider {
    position: absolute; left: 305px; top: 70px; width: 1.5px; height: 230px; background: var(--rule);
  }
  .contact-block { position: absolute; left: 335px; top: 105px; right: 20px; }
  .person-name { font-size: 32px; font-weight: 500; color: var(--gold); line-height: 1.1; }
  .person-title { font-size: 22px; margin-top: 2px; }
  .contact-list { list-style: none; margin-top: 34px; }
  .contact-list li {
    display: flex; align-items: center; gap: 10px; font-size: 18px; line-height: 1.45;
    white-space: nowrap;
  }
  .contact-list svg { width: 18px; height: 18px; flex: none; }
  .back-tagline {
    position: absolute; left: 60px; bottom: 62px; font-size: 23px; letter-spacing: .2px;
  }
</style>
</head>
<body>
<main class="sheet">
  <section class="card card-front" aria-label="Card front">
    <div class="sheen"></div>
    <div class="front-mark" aria-hidden="true"></div>
    <h1 class="front-name">TRELMOKOR ATHLETICS</h1>
    <p class="front-tagline">Personal Training &amp; Athletic Performance</p>
  </section>

  <section class="card card-back" aria-label="Card back">
    <div class="brand-block">
      <div class="back-mark" aria-hidden="true"></div>
      <p class="back-name">TrelmoKor Athletics</p>
    </div>
    <div class="divider"></div>
    <div class="contact-block">
      <h2 class="person-name">Quillan Morrow</h2>
      <p class="person-title">Owner and Trainer</p>
      <ul class="contact-list">
        <li>
          <svg viewBox="0 0 24 24" aria-hidden="true"><path fill="var(--gold)" d="M6.6 10.8a15.1 15.1 0 0 0 6.6 6.6l2.2-2.2c.3-.3.7-.4 1-.2 1.1.4 2.3.6 3.6.6.6 0 1 .4 1 1V20c0 .6-.4 1-1 1A17 17 0 0 1 3 4c0-.6.4-1 1-1h3.5c.6 0 1 .4 1 1 0 1.3.2 2.5.6 3.6.1.3 0 .7-.2 1z"/></svg>
          555.271.9384
        </li>
        <li>
          <svg viewBox="0 0 24 24" aria-hidden="true"><rect x="2.5" y="5" width="19" height="14" fill="none" stroke="var(--gold)" stroke-width="2"/><path d="M3 6l9 7 9-7M3 18l6.5-6M21 18l-6.5-6" fill="none" stroke="var(--gold)" stroke-width="1.6"/></svg>
          quillan.morrow@trelmokorathletics.com
        </li>
      </ul>
    </div>
    <p class="back-tagline">Sports Performance and Functional Strength Training</p>
  </section>
</main>
</body>
</html>
```